Full Page Ad

We are like looking for something modern, Rustic and unique for a full page ad that includes our logo, office locations, contact information. Please see our webpage and www.BRINKClaimsworks.com. I can send our logo as well.
Updates

Looking for something elegant but industrial, rustic and modern. Added Sunday, June 4, 2017

Industry/Entity Type

Insurance

Font styles to use
Serif

Requirements
Must have
• Contact information

```html
<!DOCTYPE html>
<html lang="en">
<head>
<meta charset="utf-8">
<title>Brink Claimsworks – When It Happens ad series</title>
<link href="https://fonts.googleapis.com/css2?family=Oswald:wght@500;600&family=Crimson+Text:wght@400;700&display=swap" rel="stylesheet">
<style>
  :root {
    --page: #d9d6d1;
    --navy: #1f2d5c;
    --cream-top: #efe9dc;
    --cream-bottom: #ddd3be;
    --ink: #2b2b2b;
    --muted: #8a8577;
    --accent: #e2582a;
    --frame: #ffffff;
    --rule: #b9ae96;
  }
  * { box-sizing: border-box; margin: 0; padding: 0; }
  html, body { width: 974px; height: 1200px; overflow: hidden; background: var(--page); }
  .series { position: relative; width: 974px; height: 1200px; }

  .ad {
    position: absolute; width: 369px; height: 533px; overflow: hidden;
    background: linear-gradient(180deg, var(--cream-top) 55%, var(--cream-bottom));
    box-shadow: 0 3px 10px rgba(0,0,0,.35);
    font-family: "Crimson Text", Georgia, serif; color: var(--ink);
  }
  .ad--fire { left: 62px; top: 40px; }
  .ad--accidents { left: 538px; top: 40px; }
  .ad--flood { left: 60px; top: 612px; }
  .ad--disasters { left: 538px; top: 612px; }

  .hero { position: absolute; left: 0; top: 0; width: 369px; height: 280px; }
  .ad--fire .hero { background: linear-gradient(135deg, #3b2320 0%, #7a2a24 35%, #5a4a2c 65%, #2c2421 100%); }
  .ad--accidents .hero { background: linear-gradient(180deg, #b8693a 0%, #6f7f55 20%, #2d3a55 45%, #8d949c 75%, #4b4d52 100%); }
  .ad--flood .hero { background: linear-gradient(180deg, #5f7a4a 0%, #6b4d43 30%, #8a6f5b 48%, #a5896e 60%, #9a7c5e 100%); }
  .ad--disasters .hero { background: linear-gradient(160deg, #6a5a4a 0%, #8a7a62 30%, #5d5a44 55%, #6e5f48 80%, #4c4436 100%); }

  .snapshot {
    position: absolute; left: 178px; top: 176px; width: 190px; height: 128px;
    background: var(--frame); padding: 5px; transform: rotate(-3deg);
    box-shadow: 0 2px 6px rgba(0,0,0,.4);
  }
  .snapshot--back { transform: rotate(4deg); left: 184px; top: 172px; }
  .snapshot__image { width: 100%; height: 100%; }
  .ad--fire .snapshot__image { background: linear-gradient(180deg, #c9cdd0 0%, #8e8a82 50%, #6f8a4e 100%); }
  .ad--accidents .snapshot__image { background: linear-gradient(180deg, #c43530 0%, #8fa0ad 35%, #4c5560 100%); }
  .ad--flood .snapshot__image { background: linear-gradient(180deg, #b9b8b2 0%, #6d7f8e 55%, #4e6f3a 100%); }
  .ad--disasters .snapshot__image { background: linear-gradient(180deg, #a9b2bd 0%, #e8e6df 55%, #6a9a48 100%); }

  .headline {
    position: absolute; left: 18px; top: 308px;
    font-family: "Oswald", "Arial Narrow", sans-serif; font-weight: 600;
    font-size: 15px; letter-spacing: .3px; color: var(--navy);
  }
  .peril-icon { position: absolute; left: 18px; top: 338px; width: 44px; height: 44px; fill: var(--navy); }

  .copy { position: absolute; left: 85px; top: 336px; width: 268px; font-size: 5.6px; line-height: 7px; }
  .copy p + p { margin-top: 3px; }

  .perils {
    position: absolute; left: 18px; top: 429px; list-style: none; display: flex;
    font-family: "Oswald", "Arial Narrow", sans-serif; font-weight: 500;
    font-size: 5.8px; letter-spacing: .4px; color: var(--muted);
  }
  .perils li + li::before { content: "|"; margin: 0 4px; }
  .perils .is-current { color: var(--accent); }
  .perils li.is-current + li::before, .perils li + li.is-current::before { color: var(--muted); }

  .footer { position: absolute; left: 18px; top: 464px; width: 335px; height: 60px; }
  .footer__tagline {
    position: absolute; left: 0; top: 10px; width: 190px;
    font-family: "Crimson Text", Georgia, serif; font-weight: 700;
    font-size: 6.4px; line-height: 7.2px; color: var(--navy); text-transform: uppercase;
  }
  .footer__contact { position: absolute; left: 0; top: 34px; width: 200px; font-size: 4.8px; line-height: 7px; }
  .footer__row { display: flex; justify-content: space-between; }
  .footer__web { font-weight: 700; }
  .footer__divider { position: absolute; left: 205px; top: 0; width: 1px; height: 60px; background: var(--rule); }
  .brand { position: absolute; left: 218px; top: 8px; }
  .brand__name {
    font-family: "Crimson Text", Georgia, serif; font-weight: 700;
    font-size: 13px; letter-spacing: .6px; color: var(--navy); text-transform: uppercase; white-space: nowrap;
  }
  .brand__name span { display: block; font-size: 26px; line-height: 26px; letter-spacing: 1px; }
</style>
</head>
<body>
<main class="series">

  <!-- FIRE -->
  <article class="ad ad--fire">
    <div class="hero" role="img" aria-label="Firefighters in helmets and turnout gear at a fire scene"></div>
    <div class="snapshot snapshot--back"><div class="snapshot__image"></div></div>
    <div class="snapshot"><div class="snapshot__image" role="img" aria-label="Family standing in front of their restored home"></div></div>
    <h2 class="headline">WHEN IT HAPPENS</h2>
    <svg class="peril-icon" viewBox="0 0 44 44" aria-hidden="true">
      <path d="M4 22 L20 8 L32 19 L32 40 L8 40 L8 24 Z"/>
      <rect x="15" y="24" width="9" height="9" fill="#efe9dc"/>
      <rect x="19" y="24" width="1.2" height="9"/><rect x="15" y="28" width="9" height="1.2"/>
      <path d="M34 40 C27 36 28 28 33 22 C33 27 36 27 36 24 C42 30 42 37 34 40 Z"/>
    </svg>
    <div class="copy">
      <p>BRINK retains the benefits of a large firm in our capacity to handle high volume and complex claims over a large geographical area while at the same time retaining flexibility and personal tailored service.</p>
      <p>Our staff - Our most important asset. We pride ourselves in having only the most qualified, self-motivated, trained professionals on our claim team. Our adjusting staff boasts an average experience level of over 20 years. Each of our adjusters takes advantage of the educational and training opportunities afforded to them to improve their skills and obtain industry specific designations.</p>
    </div>
    <ul class="perils"><li>ACCIDENTS</li><li>DISASTERS</li><li class="is-current">FIRE</li><li>FLOOD</li><li>WIND</li><li>PROPERTY &amp; LIABILITY</li></ul>
    <footer class="footer">
      <p class="footer__tagline">Serving you from 12 locations throughout the North East, contact us</p>
      <div class="footer__contact">
        <div class="footer__row"><span>1.800.555.0147</span><span>518.555.0162 office</span><span>888.555.0183 fax</span></div>
        <div class="footer__row"><span>PO Box 412, 20 Mill Road, Harlow Falls, NY 12099</span><span class="footer__web">www.BRINKClaimsworks.com</span></div>
      </div>
      <div class="footer__divider"></div>
      <div class="brand"><p class="brand__name"><span>BRINK</span>Claimsworks</p></div>
    </footer>
  </article>

  <!-- ACCIDENTS -->
  <article class="ad ad--accidents">
    <div class="hero" role="img" aria-label="Rear-end collision between two cars on an autumn street"></div>
    <div class="snapshot snapshot--back"><div class="snapshot__image"></div></div>
    <div class="snapshot"><div class="snapshot__image" role="img" aria-label="Driver smiling in a new car topped with a red bow"></div></div>
    <h2 class="headline">WHEN IT HAPPENS</h2>
    <svg class="peril-icon" viewBox="0 0 44 44" aria-hidden="true">
      <path d="M8 18 A14 11 0 0 1 36 18 Z"/>
      <rect x="21.4" y="18" width="1.2" height="10"/>
      <path d="M4 36 L6 30 L12 27 L30 27 L36 30 L40 32 L40 36 Z"/>
      <circle cx="12" cy="37" r="3.5"/><circle cx="32" cy="37" r="3.5"/>
      <circle cx="12" cy="37" r="1.5" fill="#efe9dc"/><circle cx="32" cy="37" r="1.5" fill="#efe9dc"/>
    </svg>
    <div class="copy">
      <p>BRINK retains the benefits of a large firm in our capacity to handle high volume and complex claims over a large geographical area while at the same time retaining flexibility and personal tailored service.</p>
      <p>Our staff - Our most important asset. We pride ourselves in having only the most qualified, self-motivated, trained professionals on our claim team. Our adjusting staff boasts an average experience level of over 20 years. Each of our adjusters takes advantage of the educational and training opportunities afforded to them to improve their skills and obtain industry specific designations.</p>
    </div>
    <ul class="perils"><li class="is-current">ACCIDENTS</li><li>DISASTERS</li><li>FIRE</li><li>FLOOD</li><li>WIND</li><li>PROPERTY &amp; LIABILITY</li></ul>
    <footer class="footer">
      <p class="footer__tagline">Serving you from 12 locations throughout the North East, contact us</p>
      <div class="footer__contact">
        <div class="footer__row"><span>1.800.555.0147</span><span>518.555.0162 office</span><span>888.555.0183 fax</span></div>
        <div class="footer__row"><span>PO Box 412, 20 Mill Road, Harlow Falls, NY 12099</span><span class="footer__web">www.BRINKClaimsworks.com</span></div>
      </div>
      <div class="footer__divider"></div>
      <div class="brand"><p class="brand__name"><span>BRINK</span>Claimsworks</p></div>
    </footer>
  </article>

  <!-- FLOOD -->
  <article class="ad ad--flood">
    <div class="hero" role="img" aria-label="Flooded street in front of a house with a submerged speed limit sign"></div>
    <div class="snapshot snapshot--back"><div class="snapshot__image"></div></div>
    <div class="snapshot"><div class="snapshot__image" role="img" aria-label="Family of four outside their dry, repaired home"></div></div>
    <h2 class="headline">WHEN IT HAPPENS</h2>
    <svg class="peril-icon" viewBox="0 0 44 44" aria-hidden="true">
      <path d="M3 22 L22 6 L41 22 L38 22 L38 41 L6 41 L6 22 Z"/>
      <rect x="15" y="20" width="14" height="14" fill="#efe9dc"/>
      <rect x="21.2" y="20" width="1.6" height="14"/><rect x="15" y="26.2" width="14" height="1.6"/>
    </svg>
    <div class="copy">
      <p>BRINK retains the benefits of a large firm in our capacity to handle high volume and complex claims over a large geographical area while at the same time retaining flexibility and personal tailored service.</p>
      <p>Our staff - Our most important asset. We pride ourselves in having only the most qualified, self-motivated, trained professionals on our claim team. Our adjusting staff boasts an average experience level of over 20 years. Each of our adjusters takes advantage of the educational and training opportunities afforded to them to improve their skills and obtain industry specific designations.</p>
    </div>
    <ul class="perils"><li>ACCIDENTS</li><li>DISASTERS</li><li>FIRE</li><li class="is-current">FLOOD</li><li>WIND</li><li>PROPERTY &amp; LIABILITY</li></ul>
    <footer class="footer">
      <p class="footer__tagline">Serving you from 12 locations throughout the North East, contact us</p>
      <div class="footer__contact">
        <div class="footer__row"><span>1.800.555.0147</span><span>518.555.0162 office</span><span>888.555.0183 fax</span></div>
        <div class="footer__row"><span>PO Box 412, 20 Mill Road, Harlow Falls, NY 12099</span><span class="footer__web">www.BRINKClaimsworks.com</span></div>
      </div>
      <div class="footer__divider"></div>
      <div class="brand"><p class="brand__name"><span>BRINK</span>Claimsworks</p></div>
    </footer>
  </article>

  <!-- DISASTERS -->
  <article class="ad ad--disasters">
    <div class="hero" role="img" aria-label="Large fallen tree crushing a car beside a damaged house after a storm"></div>
    <div class="snapshot snapshot--back"><div class="snapshot__image"></div></div>
    <div class="snapshot"><div class="snapshot__image" role="img" aria-label="Smiling family standing on the lawn of their home"></div></div>
    <h2 class="headline">WHEN IT HAPPENS</h2>
    <svg class="peril-icon" viewBox="0 0 44 44" aria-hidden="true">
      <path d="M8 22 A7 7 0 0 1 12 10 A9 9 0 0 1 28 8 A7 7 0 0 1 38 16 A6 6 0 0 1 36 24 L10 24 A5 5 0 0 1 8 22 Z"/>
      <path d="M14 26 L11 33 L15 33 L12 41 L19 31 L15 31 L18 26 Z"/>
      <path d="M26 26 L24 31 L27 31 L25 37 L30 30 L27 30 L29 26 Z"/>
      <path d="M20 27 L19 31 M33 27 L32 31 M8 27 L7 31" stroke="#1f2d5c" stroke-width="1.6" stroke-linecap="round"/>
    </svg>
    <div class="copy">
      <p>BRINK retains the benefits of a large firm in our capacity to handle high volume and complex claims over a large geographical area while at the same time retaining flexibility and personal tailored service.</p>
      <p>Our staff - Our most important asset. We pride ourselves in having only the most qualified, self-motivated, trained professionals on our claim team. Our adjusting staff boasts an average experience level of over 20 years. Each of our adjusters takes advantage of the educational and training opportunities afforded to them to improve their skills and obtain industry specific designations.</p>
    </div>
    <ul class="perils"><li>ACCIDENTS</li><li class="is-current">DISASTERS</li><li>FIRE</li><li>FLOOD</li><li>WIND</li><li>PROPERTY &amp; LIABILITY</li></ul>
    <footer class="footer">
      <p class="footer__tagline">Serving you from 12 locations throughout the North East, contact us</p>
      <div class="footer__contact">
        <div class="footer__row"><span>1.800.555.0147</span><span>518.555.0162 office</span><span>888.555.0183 fax</span></div>
        <div class="footer__row"><span>PO Box 412, 20 Mill Road, Harlow Falls, NY 12099</span><span class="footer__web">www.BRINKClaimsworks.com</span></div>
      </div>
      <div class="footer__divider"></div>
      <div class="brand"><p class="brand__name"><span>BRINK</span>Claimsworks</p></div>
    </footer>
  </article>

</main>
</body>
</html>
```